Radiology Department of an Hospital needs PowerPoint Design

The radiology Department performs X-Ray, Computed Tomography and Magnetic Resonance. We need a PowerPoint Design that includes the logo of the Hospital (file included) and our main business messages.

Target Market(s)

Business Presentations

Industry/Entity Type

Medicine

Requirements
Must have
• The logo of the Hospital (check uploaded file)

The name of the department - this is the main message:
"Serviço de Radiologia - Valmar, Lousela"

The slogan of the Department - it should go immediately bellow the name of the department in a smaller font size:
"Porque Vemos Mais Além"

The main business messages or keywords of the Department:
"Rigor"
"Segurança"
"Proximidade"
Nice to have
• The logo in all pages.
The name of the Department in all pages, with the slogan.
The keywords well visible in the first page and maybe as large watermarks on following pages.

```html
<!DOCTYPE html>
<html lang="pt">
<head>
<meta charset="utf-8">
<title>Serviço de Radiologia – Valmar, Lousela · Presentation Deck</title>
<link href="https://fonts.googleapis.com/css2?family=Montserrat:wght@400;500;600;700;800&display=swap" rel="stylesheet">
<style>
:root{
  --teal:#0f6a78;
  --teal-dark:#0a4e5a;
  --teal-light:#2a8e9a;
  --orange:#f5a800;
  --ink:#3b3b3b;
  --muted:#8a8a8a;
  --canvas:#eeeeee;
  --white:#ffffff;
  --charcoal:#333333;
}
*{box-sizing:border-box;margin:0;padding:0}
html,body{width:1200px;height:3168px;overflow:hidden;background:var(--canvas);font-family:"Montserrat",Arial,sans-serif;color:var(--ink)}
.deck{position:relative;width:1200px;height:3168px}
.slide{position:absolute;width:535px;height:301px;background:var(--white);overflow:hidden;box-shadow:0 6px 14px rgba(0,0,0,.18)}
.col-l{left:42px}.col-r{left:623px}
.r1{top:43px}.r2{top:391px}.r3{top:738px}.r4{top:1086px}.r5{top:1434px}.r6{top:1780px}.r7{top:2128px}.r8{top:2475px}.r9{top:2823px}
.abs{position:absolute}

.hdr-fade{position:absolute;left:0;top:0;width:535px;height:130px;background:linear-gradient(180deg,rgba(15,106,120,.55),rgba(15,106,120,0))}
.hdr{position:absolute;left:0;top:0;width:468px;height:48px;background:linear-gradient(90deg,#2b8d98,var(--teal));border-bottom-right-radius:48px}
.sheet{position:absolute;left:0;top:48px;width:535px;height:253px;background:var(--white);border-top-left-radius:52px}
.hdr-title{position:absolute;left:50px;top:15px;color:var(--white);font-weight:700;font-size:16px;letter-spacing:.3px}

.foot{position:absolute;left:10px;bottom:7px;line-height:1}
.foot .dept{font-size:7.5px;font-weight:700;color:var(--teal)}
.foot .slogan{font-size:4.5px;color:var(--orange);margin-top:2px}
.logo{position:absolute;display:flex;align-items:center;gap:3px}
.logo .mark{width:10px;height:10px;border-radius:50%;background:var(--orange);flex:none}
.logo .name{font-weight:600;color:var(--teal);line-height:.9;font-size:9px}
.logo.sm{right:6px;bottom:5px}
.logo.white .name{color:var(--white)}

.lorem{font-size:5.5px;line-height:1.9;color:var(--muted)}
.photo{position:absolute}

.cover-photo{left:0;top:0;width:330px;height:301px;background:linear-gradient(100deg,#e9e9e9,#f7f7f7 70%,#fff)}
.cover-curve{position:absolute;right:0;top:0;width:380px;height:58px;background:linear-gradient(90deg,rgba(15,106,120,.1),var(--teal));border-bottom-left-radius:60px}
.cover .logo{left:186px;top:76px}
.cover .logo .mark{width:34px;height:34px}
.cover .logo .name{font-size:22px;color:var(--teal)}
.cover-title{position:absolute;left:0;width:535px;top:167px;text-align:center;font-weight:700;font-size:19px;color:var(--teal)}
.cover-slogan{position:absolute;left:0;width:535px;top:193px;text-align:center;font-size:9px;color:var(--orange)}
.cover-year{position:absolute;left:0;width:535px;top:253px;text-align:center;font-size:8px;font-weight:700}
.dots{position:absolute;left:246px;top:272px;display:flex;gap:3px}
.dots span{width:11px;height:11px;border:1.2px solid var(--ink);border-radius:50%}

.s2-dark{left:0;top:0;width:200px;height:301px;background:var(--charcoal)}
.s2-teal{left:160px;top:0;width:375px;height:301px;background:linear-gradient(110deg,#cfd9db,var(--teal-light) 40%,var(--teal) 80%)}
.s2-frame{left:38px;top:46px;width:160px;height:210px;border-radius:28px;background:var(--orange)}
.s2-photo{left:40px;top:44px;width:154px;height:208px;border-radius:26px;background:linear-gradient(160deg,#f1d9a0,#e8e8e8 45%,#c9c9c9)}
.s2-title{position:absolute;right:22px;top:54px;text-align:right;color:var(--white);font-weight:700;font-size:19px;line-height:1.1}
.s2-slogan{position:absolute;right:22px;top:101px;color:var(--white);font-size:6px;letter-spacing:2.5px}
.slide .logo.s2{right:24px;top:224px}
.logo.s2 .mark{width:30px;height:30px}
.logo.s2 .name{font-size:19px}

.yr{position:absolute;width:36px;height:36px;border-radius:50%;background:var(--white);border:4px solid #ddd;display:flex;align-items:center;justify-content:center;font-size:7px;font-weight:700;box-shadow:0 2px 5px rgba(0,0,0,.2)}
.yr.teal{border-color:var(--teal)}.yr.org{border-color:var(--orange)}
.tl-line{position:absolute;left:50px;top:178px;width:450px;border-top:1px dashed #999}
.tl-text{position:absolute;width:160px;text-align:center}
.tl-text b{display:block;font-size:7px;color:var(--ink);margin-top:3px}

.card{position:absolute;top:98px;width:130px;height:170px;border-radius:16px;background:var(--white);box-shadow:0 3px 10px rgba(0,0,0,.22)}
.card .rule{position:absolute;left:8px;top:36px;height:120px;border-left:1.5px solid var(--ink)}
.card h4{position:absolute;top:33px;width:100%;text-align:center;font-size:10px;color:var(--teal)}
.card p{position:absolute;top:54px;left:22px;right:14px;text-align:center}
.hex{position:absolute;top:73px;width:46px;height:46px}

.stars{color:#e0302b;font-size:9px;letter-spacing:1px}

.bar-row{position:absolute;left:270px;width:225px}
.bar-row .lbl{font-size:7px;font-weight:600;display:flex;justify-content:space-between}
.bar-row .lbl span:last-child{font-weight:400;color:var(--muted)}
.track{height:4px;background:#ddd;border-radius:2px;margin-top:7px;position:relative}
.track i{position:absolute;left:0;top:0;height:4px;border-radius:2px}
.ring{position:absolute;width:72px;height:72px}
.ring-val{position:absolute;width:72px;text-align:center;font-size:19px;font-weight:700}

.member{position:absolute;top:95px;width:140px;text-align:center}
.avatar{width:96px;height:96px;border-radius:50%;margin:0 auto;border:5px solid var(--orange);border-bottom-color:transparent;border-left-color:transparent;padding:3px;transform:rotate(-45deg)}
.avatar div{width:100%;height:100%;border-radius:50%;background:linear-gradient(180deg,#cfcfcf,#8c8c8c)}
.member .nm{font-size:8px;font-weight:700;margin-top:12px}
.member .ps{font-size:6px;font-weight:600;letter-spacing:3px;margin-top:4px}
.member .ds{font-size:6px;line-height:1.8;margin-top:8px}

.icon-c{position:absolute;width:42px;height:42px;border-radius:50%;display:flex;align-items:center;justify-content:center;box-shadow:0 0 0 4px rgba(0,0,0,.06)}
.feat h5{font-size:9px;font-weight:600}
.feat{position:absolute;width:150px}

.org-box{position:absolute;width:100px;height:30px;border-radius:5px;display:flex;align-items:center;justify-content:center;font-size:7px}
.org-w{border:1.5px solid #bbb;background:var(--white)}
.org-g{background:#a9a9a9;color:var(--white)}
.org-o{background:var(--orange);width:100px;height:66px;flex-direction:column;gap:4px}

.badge{position:absolute;width:72px;height:38px;border-radius:6px;background:var(--white);box-shadow:0 2px 6px rgba(0,0,0,.22);display:flex;align-items:center;justify-content:center}
.badge i{display:block;width:44px;height:12px;border-radius:3px;background:#d7d7d7}

.sw-h{font-size:6px;font-weight:700;color:var(--orange)}
.sw-p{font-size:5.5px;line-height:1.45;color:var(--ink);margin-top:4px}
.sw{position:absolute;width:170px}

.ig-item{position:absolute;width:130px}
.ig-item h6{font-size:6px;font-weight:700}
.ig-item p{font-size:5px;line-height:1.4;color:var(--muted)}
.ig-ico{position:absolute;width:28px;height:28px;border-radius:4px;display:flex;align-items:center;justify-content:center}

.contact{position:absolute;left:40px;display:flex;align-items:center;gap:12px;font-size:8px;color:var(--white)}
.dept-r{position:absolute;text-align:right;line-height:1}
.dept-r .dept{font-size:7.5px;font-weight:700;color:var(--teal)}
.dept-r .slogan{font-size:4.5px;color:var(--orange);margin-top:2px}
</style>
</head>
<body>
<main class="deck">

<section class="slide col-l r1 cover">
  <div class="photo cover-photo" role="img" aria-label="Faded photo of a radiologist reviewing an X-ray"></div>
  <div class="cover-curve"></div>
  <div class="logo"><span class="mark"></span><span class="name">Vitalis<br>Hospital</span></div>
  <h1 class="cover-title">Serviço de Radiologia - Valmar, Lousela</h1>
  <p class="cover-slogan">"Porque Vemos Mais Além"</p>
  <p class="cover-year">2020</p>
  <div class="dots"><span></span><span></span><span></span></div>
</section>

<section class="slide col-r r1">
  <div class="abs s2-dark"></div>
  <div class="abs s2-teal"></div>
  <div class="abs s2-frame"></div>
  <div class="photo s2-photo" role="img" aria-label="Photo of a smiling doctor holding an X-ray film"></div>
  <h2 class="s2-title">Serviço de Radiologia<br>Valmar, Lousela</h2>
  <p class="s2-slogan">"Porque Vemos Mais Além"</p>
  <div class="logo white s2"><span class="mark"></span><span class="name">Vitalis<br>Hospital</span></div>
</section>

<section class="slide col-l r2">
  <div class="hdr-fade"></div><div class="hdr"></div><div class="sheet"></div>
  <h2 class="hdr-title">ABOUT US</h2>
  <svg class="abs" style="left:36px;top:75px" width="20" height="20" viewBox="0 0 20 20"><rect x="3" y="5" width="14" height="14" fill="none" stroke="#0f6a78" stroke-width="2"/><rect x="7" y="1" width="6" height="5" fill="#0f6a78"/><rect x="8.5" y="12" width="3" height="7" fill="#0f6a78"/></svg>
  <p class="abs lorem" style="left:36px;top:100px;width:222px;text-align:justify">Lorem ipsum dolor sit amet, consectetuer adipiscing elit, sed diam nonummy nibh euismod tincidunt ut laoreet dolore magna aliquam erat volutpat. Ut wisi enim ad minim veniam, quis nostrud exerci tation ullamcorper suscipit lobortis nisl ut aliquip ex ea commodo consequat. Duis autem vel eum iriure dolor in hendrerit in vulputate velit esse molestie consequat, vel illum dolore eu feugiat nulla facilisis at vero eros et accumsan et iusto odio dignissim qui blandit praesent luptatum zzril delenit augue duis dolore te feugait nulla facilisi.</p>
  <div class="photo" style="left:265px;top:67px;width:270px;height:210px;border-top-left-radius:36px;background:linear-gradient(135deg,#f2f2f2,#d9dde0 55%,#b9c2c6)" role="img" aria-label="Photo of a stethoscope and pen on a medical form"></div>
  <div class="foot"><p class="dept">Serviço de Radiologia - Valmar, Lousela</p><p class="slogan">"Porque Vemos Mais Além"</p></div>
  <div class="logo sm"><span class="mark"></span><span class="name">Vitalis<br>Hospital</span></div>
</section>

<section class="slide col-r r2">
  <div class="hdr-fade"></div><div class="hdr"></div><div class="sheet"></div>
  <h2 class="hdr-title">OUR ROADMAP</h2>
  <div class="tl-text" style="left:22px;top:64px"><p class="lorem" style="line-height:1.7">sit amet, consectetuer adipiscing elit, sed<br>diam nonummy nibh euismod tincidunt</p><b>LOREM IPSUM DOLOR</b></div>
  <div class="tl-text" style="left:235px;top:64px"><p class="lorem" style="line-height:1.7">sit amet, consectetuer adipiscing elit, sed<br>diam nonummy nibh euismod tincidunt</p><b>LOREM IPSUM DOLOR</b></div>
  <div class="tl-line"></div>
  <div class="yr" style="left:72px;top:160px">2018</div>
  <div class="yr teal" style="left:178px;top:160px">2019</div>
  <div class="yr" style="left:285px;top:160px">2020</div>
  <div class="yr org" style="left:392px;top:160px">2021</div>
  <div class="tl-text" style="left:116px;top:222px"><b>LOREM IPSUM DOLOR</b><p class="lorem" style="line-height:1.7">sit amet, consectetuer adipiscing elit, sed<br>diam nonummy nibh euismod tincidunt</p></div>
  <div class="tl-text" style="left:330px;top:222px"><b>LOREM IPSUM DOLOR</b><p class="lorem" style="line-height:1.7">sit amet, consectetuer adipiscing elit, sed<br>diam nonummy nibh euismod tincidunt</p></div>
  <div class="foot"><p class="dept">Serviço de Radiologia - Valmar, Lousela</p><p class="slogan">"Porque Vemos Mais Além"</p></div>
  <div class="logo sm"><span class="mark"></span><span class="name">Vitalis<br>Hospital</span></div>
</section>

<section class="slide col-l r3">
  <div class="hdr-fade"></div><div class="hdr"></div><div class="sheet"></div>
  <h2 class="hdr-title">OUR VISION, VALUE &amp; GOAL</h2>
  <div class="card" style="left:44px"><div class="rule"></div><h4>Lorem ipsum</h4><p class="lorem" style="line-height:1.6">Lorem ipsum dolor sit amet, consectetuer adipiscing elit, sed diam nonummy nibh euismod tincidunt ut laoreet dolore magna aliquam erat volutpat.</p></div>
  <div class="card" style="left:202px"><div class="rule"></div><h4 style="color:var(--ink)">Lorem ipsum</h4><p class="lorem" style="line-height:1.6">Lorem ipsum dolor sit amet, consectetuer adipiscing elit, sed diam nonummy nibh euismod tincidunt ut laoreet dolore magna aliquam erat volutpat.</p></div>
  <div class="card" style="left:360px"><div class="rule"></div><h4 style="color:#777">Lorem ipsum</h4><p class="lorem" style="line-height:1.6">Lorem ipsum dolor sit amet, consectetuer adipiscing elit, sed diam nonummy nibh euismod tincidunt ut laoreet dolore magna aliquam erat volutpat.</p></div>
  <svg class="hex" style="left:86px" viewBox="0 0 46 46"><polygon points="23,1 43,12 43,34 23,45 3,34 3,12" fill="#0f6a78" stroke="#fff" stroke-width="3"/><ellipse cx="23" cy="23" rx="10" ry="6" fill="none" stroke="#fff" stroke-width="2"/><circle cx="23" cy="23" r="3" fill="#fff"/></svg>
  <svg class="hex" style="left:244px" viewBox="0 0 46 46"><polygon points="23,1 43,12 43,34 23,45 3,34 3,12" fill="#f5a800" stroke="#fff" stroke-width="3"/><circle cx="23" cy="23" r="9" fill="none" stroke="#fff" stroke-width="2"/><circle cx="23" cy="23" r="4" fill="#fff"/></svg>
  <svg class="hex" style="left:402px" viewBox="0 0 46 46"><polygon points="23,1 43,12 43,34 23,45 3,34 3,12" fill="#8a8a8a" stroke="#fff" stroke-width="3"/><circle cx="23" cy="23" r="8" fill="none" stroke="#fff" stroke-width="2"/><path d="M23 11v24M11 23h24" stroke="#fff" stroke-width="1.5"/></svg>
  <div class="foot"><p class="dept">Serviço de Radiologia - Valmar, Lousela</p><p class="slogan">"Porque Vemos Mais Além"</p></div>
  <div class="logo sm"><span class="mark"></span><span class="name">Vitalis<br>Hospital</span></div>
</section>

<section class="slide col-r r3">
  <div class="abs" style="left:0;top:0;width:535px;height:301px;background:linear-gradient(90deg,rgba(15,106,120,.55),rgba(15,106,120,0) 45%)"></div>
  <div class="abs" style="left:0;top:0;width:445px;height:52px;background:var(--teal);border-bottom-right-radius:50px"></div>
  <div class="abs" style="left:45px;top:74px;width:114px;height:172px;background:#2f2f2f;border-radius:24px 0 24px 0;padding:14px 16px;color:#fff">
    <p style="font-size:19px;font-weight:700;line-height:1.1;text-align:center">Title<br>Slide</p>
    <p style="font-size:7px;text-align:center;margin-top:3px">(Testimonials)</p>
    <p style="font-size:6px;line-height:1.8;margin-top:20px">Lorem Ipsum is simply dummy text of the printing and typesetting industry</p>
  </div>
  <svg class="abs" style="left:170px;top:80px" width="330" height="100" viewBox="0 0 330 100"><path d="M0 2H270v34" fill="none" stroke="#555" stroke-width="1"/><path d="M0 26H195v44" fill="none" stroke="#555" stroke-width="1"/><path d="M0 51H45v44" fill="none" stroke="#555" stroke-width="1"/><circle cx="2" cy="2" r="5" fill="#0f6a78"/><circle cx="2" cy="26" r="5" fill="#555"/><circle cx="2" cy="51" r="5" fill="#f5a800"/></svg>
  <div class="abs" style="left:187px;top:163px;width:78px;height:125px;background:#fff;box-shadow:0 3px 8px rgba(0,0,0,.25);padding:10px 8px 0">
    <p class="lorem" style="line-height:2.1;color:#555">Lorem ipsum is simply dummy text of the printing and typesetting industry</p><p class="stars">★★★★★</p>
    <div class="abs" style="left:0;bottom:0;width:78px;height:20px;background:var(--orange);color:#fff;font-size:7px;display:flex;align-items:center;justify-content:center">Lorem ipsum</div></div>
  <div class="abs" style="left:300px;top:137px;width:78px;height:125px;background:#fff;box-shadow:0 3px 8px rgba(0,0,0,.25);padding:10px 8px 0">
    <p class="lorem" style="line-height:2.1;color:#555">Lorem ipsum is simply dummy text of the printing and typesetting industry</p><p class="stars">★★★★★</p>
    <div class="abs" style="left:0;bottom:0;width:78px;height:20px;background:#2f2f2f;color:#fff;font-size:7px;display:flex;align-items:center;justify-content:center">Lorem ipsum</div></div>
  <div class="abs" style="left:413px;top:106px;width:78px;height:125px;background:#fff;box-shadow:0 3px 8px rgba(0,0,0,.25);padding:10px 8px 0">
    <p class="lorem" style="line-height:2.1;color:#555">Lorem ipsum is simply dummy text of the printing and typesetting industry</p><p class="stars">★★★★★</p>
    <div class="abs" style="left:0;bottom:0;width:78px;height:20px;background:var(--teal);color:#fff;font-size:7px;display:flex;align-items:center;justify-content:center">Lorem ipsum</div></div>
  <div class="logo sm"><span class="mark"></span><span class="name">Vitalis<br>Hospital</span></div>
</section>

<section class="slide col-l r4">
  <div class="hdr-fade"></div><div class="hdr"></div><div class="sheet"></div>
  <h2 class="hdr-title">MEDICAL INFOGRAPHIC</h2>
  <svg class="ring" style="left:40px;top:78px" viewBox="0 0 72 72"><circle cx="36" cy="36" r="31" fill="#fff" stroke="#e6e6e6" stroke-width="6"/><circle cx="36" cy="36" r="31" fill="none" stroke="#0f6a78" stroke-width="6" stroke-dasharray="142 195" transform="rotate(-90 36 36)"/></svg>
  <p class="ring-val" style="left:40px;top:101px;color:var(--teal)">73%</p>
  <svg class="ring" style="left:40px;top:171px" viewBox="0 0 72 72"><circle cx="36" cy="36" r="31" fill="#fff" stroke="#e6e6e6" stroke-width="6"/><circle cx="36" cy="36" r="31" fill="none" stroke="#f5a800" stroke-width="6" stroke-dasharray="97 195" transform="rotate(-90 36 36)"/></svg>
  <p class="ring-val" style="left:40px;top:194px;color:var(--orange)">50%</p>
  <div class="abs" style="left:135px;top:96px;width:95px"><p style="font-size:7px;font-weight:700;color:var(--teal)">PROJECT 01</p><p class="lorem" style="line-height:1.8">Lorem Ipsum is simply dummy text of the printing and typesetting industry</p></div>
  <div class="abs" style="left:135px;top:189px;width:95px"><p style="font-size:7px;font-weight:700;color:var(--orange)">PROJECT 02</p><p class="lorem" style="line-height:1.8">Lorem Ipsum is simply dummy text of the printing and typesetting industry</p></div>
  <div class="bar-row" style="top:80px"><p class="lbl"><span>PROJECT 03</span><span>32%</span></p><div class="track"><i style="width:32%;background:#bbb"></i></div></div>
  <div class="bar-row" style="top:115px"><p class="lbl"><span>PROJECT 04</span><span>72%</span></p><div class="track"><i style="width:72%;background:var(--teal)"></i></div></div>
  <div class="bar-row" style="top:151px"><p class="lbl"><span>PROJECT 05</span><span>52%</span></p><div class="track"><i style="width:52%;background:var(--orange)"></i></div></div>
  <div class="bar-row" style="top:186px"><p class="lbl"><span>PROJECT 06</span><span>12%</span></p><div class="track"><i style="width:12%;background:var(--teal)"></i></div></div>
  <div class="bar-row" style="top:222px"><p class="lbl"><span>PROJECT 07</span><span>60%</span></p><div class="track"><i style="width:60%;background:var(--orange)"></i></div></div>
  <div class="foot"><p class="dept">Serviço de Radiologia - Valmar, Lousela</p><p class="slogan">"Porque Vemos Mais Além"</p></div>
  <div class="logo sm"><span class="mark"></span><span class="name">Vitalis<br>Hospital</span></div>
</section>

<section class="slide col-r r4">
  <div class="photo" style="left:0;top:0;width:535px;height:140px;background:linear-gradient(90deg,#d8d8d8,#9a9a9a 45%,#cfcfcf)" role="img" aria-label="Grayscale photo of a doctor and patients in a hospital corridor"></div>
  <div class="logo white" style="right:10px;top:96px"><span class="mark" style="width:20px;height:20px"></span><span class="name" style="font-size:15px">Vitalis<br>Hospital</span></div>
  <div class="abs" style="left:0;top:140px;width:120px;height:161px;background:linear-gradient(90deg,var(--teal-light),var(--teal))"></div>
  <div class="abs" style="left:117px;top:140px;width:418px;height:161px;background:#fff;border-top-left-radius:34px;border-left:4px solid var(--orange)"></div>
  <p class="abs" style="left:20px;top:180px;color:#fff;font-weight:700;font-size:16px;line-height:1.2">OUR<br>MISSION</p>
  <p class="abs lorem" style="left:163px;top:166px;width:348px;text-align:justify;line-height:2.2;color:#555">Lorem ipsum dolor sit amet, consectetuer adipiscing elit, sed diam nonummy nibh euismod tincidunt ut laoreet dolore magna aliquam erat volutpat. Ut wisi enim ad minim veniam, quis nostrud exerci tation ullamcorper suscipit lobortis nisl ut aliquip ex ea commodo consequat. Duis autem vel eum iriure dolor in hendrerit in vulputate velit esse molestie consequat, vel illum dolore eu feugiat nulla facilisis at vero eros et accumsan et iusto odio dignissim qui blandit praesent luptatum zzril delenit augue duis dolore te feugait nulla facilisi.</p>
  <div class="dept-r" style="right:6px;bottom:7px"><p class="dept">Serviço de Radiologia - Valmar, Lousela</p><p class="slogan">"Porque Vemos Mais Além"</p></div>
</section>

<section class="slide col-l r5">
  <div class="abs" style="left:0;top:0;width:535px;height:200px;background:linear-gradient(90deg,rgba(15,106,120,.35),var(--teal))"></div>
  <div class="abs" style="left:0;top:100px;width:535px;height:201px;background:#fff;border-top-left-radius:60px;border-top-right-radius:60px"></div>
  <h2 class="abs" style="left:0;width:535px;top:22px;text-align:center;color:#fff;font-size:16px;font-weight:700">OUR TEAM</h2>
  <div class="abs" style="left:247px;top:47px;width:40px;border-top:2px solid #fff"></div>
  <div class="member" style="left:43px"><div class="avatar"><div role="img" aria-label="Team member portrait photo"></div></div><p class="nm">NAME</p><p class="ps">POTITION</p><p class="ds">Lorem ipsum dolor sit amet, consectetuer adipiscing elit, sed diam nonummy nibh</p></div>
  <div class="member" style="left:197px"><div class="avatar"><div role="img" aria-label="Team member portrait photo"></div></div><p class="nm">NAME</p><p class="ps" style="color:var(--teal)">POTITION</p><p class="ds" style="color:var(--teal)">Lorem ipsum dolor sit amet, consectetuer adipiscing elit, sed diam nonummy nibh</p></div>
  <div class="member" style="left:348px"><div class="avatar"><div role="img" aria-label="Team member portrait photo"></div></div><p class="nm" style="color:#666">NAME</p><p class="ps" style="color:#666">POTITION</p><p class="ds" style="color:#777">Lorem ipsum dolor sit amet, consectetuer adipiscing elit, sed diam nonummy nibh</p></div>
  <div class="foot"><p class="dept">Serviço de Radiologia - Valmar, Lousela</p><p class="slogan">"Porque Vemos Mais Além"</p></div>
  <div class="logo sm"><span class="mark"></span><span class="name">Vitalis<br>Hospital</span></div>
</section>

<section class="slide col-r r5">
  <div class="abs" style="left:-150px;top:-70px;width:372px;height:372px;border-radius:50%;background:var(--teal)"></div>
  <div class="photo" style="left:-150px;top:-60px;width:355px;height:355px;border-radius:50%;background:linear-gradient(135deg,#a7b4b8,#5f6d71 60%,#3c4649)" role="img" aria-label="Photo of an empty hospital room with a bed"></div>
  <p class="abs" style="left:14px;top:128px;color:#fff;font-size:17px;font-weight:600">Segurança</p>
  <div class="abs" style="left:14px;top:154px;width:44px;border-top:2px solid #fff"></div>
  <svg class="abs" style="left:16px;top:162px" width="18" height="20" viewBox="0 0 18 20"><path d="M3 1v7a5 5 0 0 0 10 0V1M8 13v3a4 4 0 0 0 8 0v-4" fill="none" stroke="#fff" stroke-width="1.6"/></svg>
  <svg class="abs" style="left:246px;top:8px" width="70" height="290" viewBox="0 0 70 290"><path d="M40 10 Q85 145 40 280" fill="none" stroke="#777" stroke-width="1"/></svg>
  <div class="dept-r" style="right:4px;top:5px"><p class="dept">Serviço de Radiologia - Valmar, Lousela</p><p class="slogan">"Porque Vemos Mais Além"</p></div>
  <div class="icon-c" style="left:263px;top:24px;background:var(--teal)"><svg width="22" height="22" viewBox="0 0 22 22"><path d="M8 2h6v6h6v6h-6v6H8v-6H2V8h6z" fill="none" stroke="#fff" stroke-width="1.6"/></svg></div>
  <div class="feat" style="left:316px;top:26px"><h5>Lorem ipsum</h5><p class="lorem" style="line-height:1.4">Lorem ipsum dolor sit amet, consectetuer adipiscing elit,</p></div>
  <div class="icon-c" style="left:293px;top:93px;background:var(--teal)"><svg width="22" height="22" viewBox="0 0 22 22"><rect x="2" y="3" width="18" height="14" fill="none" stroke="#fff" stroke-width="1.6"/><path d="M4 11h4l2-4 3 7 2-3h3" fill="none" stroke="#fff" stroke-width="1.4"/></svg></div>
  <div class="feat" style="left:346px;top:96px"><h5>Lorem ipsum</h5><p class="lorem" style="line-height:1.4">Lorem ipsum dolor sit amet, consectetuer adipiscing elit,</p></div>
  <div class="icon-c" style="left:293px;top:163px;background:var(--orange)"><svg width="22" height="22" viewBox="0 0 22 22"><circle cx="11" cy="11" r="9" fill="none" stroke="#333" stroke-width="1.6"/><circle cx="11" cy="11" r="2.5" fill="#333"/></svg></div>
  <div class="feat" style="left:346px;top:165px"><h5>Lorem ipsum</h5><p class="lorem" style="line-height:1.4">Lorem ipsum dolor sit amet, consectetuer adipiscing elit,</p></div>
  <div class="icon-c" style="left:263px;top:232px;background:var(--teal)"><svg width="22" height="22" viewBox="0 0 22 22"><path d="M5 18h12M7 18v-6a4 4 0 0 1 8 0v6M11 2v3M3 6l2 2M19 6l-2 2" fill="none" stroke="#fff" stroke-width="1.6"/></svg></div>
  <div class="feat" style="left:323px;top:235px"><h5>Lorem ipsum</h5><p class="lorem" style="line-height:1.4">Lorem ipsum dolor sit amet, consectetuer adipiscing elit,</p></div>
  <div class="logo sm"><span class="mark"></span><span class="name">Vitalis<br>Hospital</span></div>
</section>

<section class="slide col-l r6">
  <div class="abs" style="left:280px;top:0;width:255px;height:301px;background:linear-gradient(180deg,rgba(15,106,120,.1),var(--teal))"></div>
  <div class="abs" style="left:0;top:0;width:480px;height:301px;background:#fff;border-bottom-right-radius:60px;border-top-right-radius:60px"></div>
  <div class="photo" style="left:346px;top:50px;width:189px;height:190px;background:linear-gradient(135deg,#4a4a4a,#9a9a9a 50%,#f0f0f0)" role="img" aria-label="Photo of a doctor examining X-ray films on a light box"></div>
  <h2 class="abs" style="left:40px;top:58px;font-size:19px;font-weight:700">X-RAY TEST</h2>
  <p class="abs" style="left:40px;top:86px;font-size:7px;letter-spacing:3px;color:#777">SUBTITLE GOES HERE</p>
  <p class="abs" style="left:40px;top:112px;width:270px;font-size:5.8px;line-height:2.3;text-align:justify">Lorem ipsum dolor sit amet, consectetuer adipiscing elit, sed diam nonummy nibh euismod tincidunt ut laoreet dolore magna aliquam erat volutpat. Ut wisi enim ad minim veniam, quis nostrud exerci tation ullamcorper suscipit lobortis nisl ut aliquip ex ea commodo consequat. Duis autem vel eum iriure dolor in hendrerit in vulputate velit esse molestie consequat, vel illum dolore eu feugiat nulla facilisis at vero eros et accumsan et iusto odio dignissim qui blandit praesent luptatum zzril delenit augue duis dolore te feugait nulla facilisi.</p>
  <div class="logo" style="left:10px;bottom:7px"><span class="mark"></span><span class="name">Vitalis<br>Hospital</span></div>
  <div class="dept-r" style="left:245px;bottom:7px"><p class="dept">Serviço de Radiologia - Valmar, Lousela</p><p class="slogan">"Porque Vemos Mais Além"</p></div>
</section>

<section class="slide col-r r6">
  <h2 class="abs" style="left:0;width:535px;top:14px;text-align:center;font-size:16px;font-weight:700;color:var(--teal)">HOSPITAL MANAGEMENT</h2>
  <div class="abs" style="left:48px;top:53px;width:442px;height:230px;border:1px dashed #aaa;border-radius:16px"></div>
  <div class="abs" style="left:111px;top:62px;width:312px;height:60px;background:var(--teal);border-radius:6px"></div>
  <div class="logo white" style="left:210px;top:79px"><span class="mark" style="width:20px;height:20px"></span><span class="name" style="font-size:15px">Vitalis<br>Hospital</span></div>
  <svg class="abs" style="left:0;top:0" width="535" height="301" viewBox="0 0 535 301"><path d="M193 122V210h-28M189 122V140h-24M215 140v144" fill="none" stroke="#d33" stroke-width="1" stroke-dasharray="2 2"/><path d="M325 122v126M330 122v126M335 122v126M325 145h25M330 181h20M335 217h15M340 122v126h10" fill="none" stroke="#777" stroke-width="1"/></svg>
  <div class="org-box org-o" style="left:65px;top:128px"><svg width="12" height="14" viewBox="0 0 12 14"><circle cx="6" cy="4" r="3" fill="none" stroke="#fff" stroke-width="1.3"/><path d="M1 13a5 5 0 0 1 10 0z" fill="none" stroke="#fff" stroke-width="1.3"/></svg>Lorem ipsum</div>
  <div class="org-box org-o" style="left:65px;top:200px"><svg width="12" height="14" viewBox="0 0 12 14"><circle cx="6" cy="4" r="3" fill="none" stroke="#fff" stroke-width="1.3"/><path d="M1 13a5 5 0 0 1 10 0z" fill="none" stroke="#fff" stroke-width="1.3"/></svg>Lorem ipsum</div>
  <div class="org-box org-w" style="left:219px;top:130px">Lorem ipsum</div>
  <div class="org-box org-w" style="left:219px;top:166px">Lorem ipsum</div>
  <div class="org-box org-w" style="left:219px;top:202px">Lorem ipsum</div>
  <div class="org-box org-w" style="left:219px;top:238px">Lorem ipsum</div>
  <div class="org-box org-g" style="left:368px;top:130px">Lorem ipsum</div>
  <div class="org-box org-g" style="left:368px;top:166px">Lorem ipsum</div>
  <div class="org-box org-g" style="left:368px;top:202px">Lorem ipsum</div>
  <div class="org-box org-g" style="left:368px;top:238px">Lorem ipsum</div>
</section>

<section class="slide col-l r7">
  <div class="photo" style="left:0;top:0;width:535px;height:301px;background:radial-gradient(circle at 55% 55%,#2f7fbf,#0d4a86 45%,#082c56)" role="img" aria-label="Photo of an MRI scanner in blue light"></div>
  <div class="abs" style="left:64px;top:43px;width:306px;height:193px;border:1.5px solid rgba(255,255,255,.75);border-radius:10px;background:rgba(255,255,255,.06)"></div>
  <svg class="abs" style="left:82px;top:162px" width="22" height="18" viewBox="0 0 22 18"><path d="M2 12h18M4 12V6h6l4 6M6 16h10" fill="none" stroke="#fff" stroke-width="1.6"/></svg>
  <p class="abs" style="left:80px;top:182px;color:#fff;font-size:16px;font-weight:700">BUSINESS MESSAGES</p>
  <div class="abs" style="left:80px;top:206px;width:46px;border-top:2px solid #fff"></div>
  <div class="logo white" style="right:14px;top:16px"><span class="mark"></span><span class="name">Vitalis<br>Hospital</span></div>
</section>

<section class="slide col-r r7">
  <div class="abs" style="left:0;top:0;width:535px;height:130px;background:linear-gradient(90deg,var(--teal),rgba(15,106,120,.2))"></div>
  <div class="abs" style="left:0;top:48px;width:535px;height:253px;background:#fff;border-top-left-radius:52px"></div>
  <div class="abs" style="left:468px;top:0;width:67px;height:48px;background:#fff;border-bottom-left-radius:48px"></div>
  <h2 class="hdr-title" style="left:42px">OUR PARTNERS</h2>
  <div class="badge" style="left:82px;top:92px"><i></i></div>
  <div class="badge" style="left:176px;top:92px"><i></i></div>
  <div class="badge" style="left:270px;top:92px"><i></i></div>
  <div class="badge" style="left:364px;top:92px"><i></i></div>
  <div class="badge" style="left:82px;top:143px"><i></i></div>
  <div class="badge" style="left:176px;top:143px"><i></i></div>
  <div class="badge" style="left:270px;top:143px"><i></i></div>
  <div class="badge" style="left:364px;top:143px"><i></i></div>
  <div class="badge" style="left:82px;top:193px"><i></i></div>
  <div class="badge" style="left:176px;top:193px"><i></i></div>
  <div class="badge" style="left:270px;top:193px"><i></i></div>
  <div class="badge" style="left:364px;top:193px"><p style="font-size:5px;text-align:center;line-height:1.3">ADD YOUR LOGO<br>HERE</p></div>
  <div class="foot"><p class="dept">Serviço de Radiologia - Valmar, Lousela</p><p class="slogan">"Porque Vemos Mais Além"</p></div>
  <div class="logo sm"><span class="mark"></span><span class="name">Vitalis<br>Hospital</span></div>
</section>

<section class="slide col-l r8">
  <div class="hdr-fade"></div><div class="hdr"></div><div class="sheet"></div>
  <h2 class="hdr-title">OUR ANALYSIS</h2>
  <svg class="abs" style="left:203px;top:95px" width="130" height="130" viewBox="0 0 130 130">
    <path d="M65 65 L38 38 A38 38 0 0 1 92 38 Z" fill="#f5a800"/><path d="M65 65 L92 38 A38 38 0 0 1 92 92 Z" fill="#0f6a78"/><path d="M65 65 L92 92 A38 38 0 0 1 38 92 Z" fill="#f5a800"/><path d="M65 65 L38 92 A38 38 0 0 1 38 38 Z" fill="#0f6a78"/>
    <circle cx="65" cy="32" r="17" fill="#f5a800"/><circle cx="98" cy="65" r="17" fill="#0f6a78"/><circle cx="65" cy="98" r="17" fill="#f5a800"/><circle cx="32" cy="65" r="17" fill="#0f6a78"/>
    <circle cx="65" cy="32" r="12" fill="#fff"/><circle cx="98" cy="65" r="12" fill="#fff"/><circle cx="65" cy="98" r="12" fill="#fff"/><circle cx="32" cy="65" r="12" fill="#fff"/>
    <circle cx="65" cy="65" r="10" fill="#fff"/><circle cx="65" cy="65" r="5" fill="#f5a800"/>
    <text x="65" y="37" text-anchor="middle" font-family="Montserrat,sans-serif" font-size="14" fill="#333">S</text>
    <text x="98" y="70" text-anchor="middle" font-family="Montserrat,sans-serif" font-size="14" fill="#333">W</text>
    <text x="65" y="103" text-anchor="middle" font-family="Montserrat,sans-serif" font-size="14" fill="#333">O</text>
    <text x="32" y="70" text-anchor="middle" font-family="Montserrat,sans-serif" font-size="14" fill="#333">T</text>
  </svg>
  <div class="sw" style="left:18px;top:100px;text-align:right"><p class="sw-h">STRENGTH</p><p class="sw-p">Lorem ipsum dolor sit amet, consectetuer adipiscing elit, sed diam nonummy nibh euismod tincidunt ut laoreet dolore magna aliquam erat</p></div>
  <div class="sw" style="left:346px;top:100px"><p class="sw-h">WEAKNESS</p><p class="sw-p">Lorem ipsum dolor sit amet, consectetuer adipiscing elit, sed diam nonummy nibh euismod tincidunt ut laoreet dolore magna aliquam erat</p></div>
  <div class="sw" style="left:18px;top:213px;text-align:right"><p class="sw-h">THREAT</p><p class="sw-p">Lorem ipsum dolor sit amet, consectetuer adipiscing elit, sed diam nonummy nibh euismod tincidunt ut laoreet dolore magna aliquam erat</p></div>
  <div class="sw" style="left:346px;top:213px"><p class="sw-h">OPPORTUNITY</p><p class="sw-p">Lorem ipsum dolor sit amet, consectetuer adipiscing elit, sed diam nonummy nibh euismod tincidunt ut laoreet dolore magna aliquam erat</p></div>
  <div class="foot"><p class="dept">Serviço de Radiologia - Valmar, Lousela</p><p class="slogan">"Porque Vemos Mais Além"</p></div>
  <div class="logo sm"><span class="mark"></span><span class="name">Vitalis<br>Hospital</span></div>
</section>

<section class="slide col-r r8">
  <div class="hdr-fade"></div><div class="hdr"></div><div class="sheet"></div>
  <h2 class="hdr-title">INFOGRAPHIC</h2>
  <svg class="abs" style="left:0;top:0" width="535" height="301" viewBox="0 0 535 301">
    <circle cx="265" cy="170" r="62" fill="#fff" stroke="#0a4e5a" stroke-width="3"/>
    <g fill="none" stroke="#333" stroke-width="1" stroke-dasharray="2 2"><path d="M130 90H165L210 140M130 159H203M130 226H165L210 200M400 90H365L320 140M400 159H327M400 226H365L320 200"/></g>
  </svg>
  <div class="logo" style="left:225px;top:158px"><span class="mark" style="width:16px;height:16px"></span><span class="name" style="font-size:13px">Vitalis<br>Hospital</span></div>
  <div class="ig-ico" style="left:80px;top:76px;background:var(--teal)"><svg width="16" height="16" viewBox="0 0 16 16"><path d="M3 13l10-10M5 3h8v8" fill="none" stroke="#fff" stroke-width="1.5"/></svg></div>
  <div class="ig-item" style="left:134px;top:78px"><h6>LOREM IPSUM</h6><p>Lorem ipsum dolor sit<br>amet, consectetuer</p></div>
  <div class="ig-ico" style="left:80px;top:145px;background:var(--orange)"><svg width="16" height="16" viewBox="0 0 16 16"><rect x="3" y="3" width="10" height="10" fill="none" stroke="#fff" stroke-width="1.5"/><path d="M8 5v6M5 8h6" stroke="#fff" stroke-width="1.5"/></svg></div>
  <div class="ig-item" style="left:134px;top:145px"><h6 style="color:var(--orange)">LOREM IPSUM</h6><p>Lorem ipsum dolor sit<br>amet, consectetuer</p></div>
  <div class="ig-ico" style="left:80px;top:212px;background:var(--teal)"><svg width="16" height="16" viewBox="0 0 16 16"><circle cx="8" cy="8" r="5.5" fill="none" stroke="#fff" stroke-width="1.5"/><path d="M8 5v3l2 2" fill="none" stroke="#fff" stroke-width="1.5"/></svg></div>
  <div class="ig-item" style="left:134px;top:213px"><h6>LOREM IPSUM</h6><p>Lorem ipsum dolor sit<br>amet, consectetuer</p></div>
  <div class="ig-ico" style="left:427px;top:76px;background:var(--teal)"><svg width="16" height="16" viewBox="0 0 16 16"><circle cx="8" cy="8" r="5.5" fill="none" stroke="#fff" stroke-width="1.5"/><circle cx="8" cy="8" r="2" fill="#fff"/></svg></div>
  <div class="ig-item" style="left:330px;top:78px;width:90px;text-align:right"><h6>LOREM IPSUM</h6><p>Lorem ipsum dolor sit<br>amet, consectetuer</p></div>
  <div class="ig-ico" style="left:427px;top:145px;background:var(--orange)"><svg width="16" height="16" viewBox="0 0 16 16"><path d="M3 8h10M8 3v10" stroke="#fff" stroke-width="2"/></svg></div>
  <div class="ig-item" style="left:330px;top:145px;width:90px;text-align:right"><h6 style="color:var(--orange)">LOREM IPSUM</h6><p>Lorem ipsum dolor sit<br>amet, consectetuer</p></div>
  <div class="ig-ico" style="left:427px;top:212px;background:var(--teal)"><svg width="16" height="16" viewBox="0 0 16 16"><path d="M8 2l1.8 4 4.2.4-3.2 2.8 1 4.2L8 11.2 4.2 13.4l1-4.2L2 6.4 6.2 6z" fill="none" stroke="#fff" stroke-width="1.3"/></svg></div>
  <div class="ig-item" style="left:330px;top:213px;width:90px;text-align:right"><h6>LOREM IPSUM</h6><p>Lorem ipsum dolor sit<br>amet, consectetuer</p></div>
  <div class="foot"><p class="dept">Serviço de Radiologia - Valmar, Lousela</p><p class="slogan">"Porque Vemos Mais Além"</p></div>
  <div class="logo sm"><span class="mark"></span><span class="name">Vitalis<br>Hospital</span></div>
</section>

<section class="slide col-l r9">
  <h2 class="abs" style="left:0;width:535px;top:24px;text-align:center;font-size:13px;font-weight:700;color:var(--teal)">FREE EDITABLE VECTOR ICON LINKS AVAILABLE</h2>
  <div class="abs" style="left:26px;top:60px;width:485px;height:222px;background:linear-gradient(135deg,#d6e8eb,#c3dde1);border-radius:4px" role="img" aria-label="Grid of editable medical line icons"></div>
</section>

<section class="slide col-r r9">
  <div class="abs" style="left:0;top:100px;width:535px;height:201px;background:linear-gradient(90deg,var(--teal-light),var(--teal-dark))" role="img" aria-label="Faded teal-toned photo of a medical professional"></div>
  <div class="abs" style="left:0;top:0;width:535px;height:138px;background:#fff;border-bottom-right-radius:70px"></div>
  <h2 class="abs" style="left:52px;top:42px;font-size:20px;font-weight:700;color:var(--teal)">THANK YOU</h2>
  <div class="abs" style="left:52px;top:72px;width:56px;border-top:2px solid var(--orange)"></div>
  <p class="abs" style="left:40px;top:166px;color:#fff;font-size:9px;font-weight:600">PRESENTER NAME</p>
  <div class="contact" style="top:188px"><svg width="12" height="12" viewBox="0 0 12 12"><path d="M2 1h3l1 3-2 1a7 7 0 0 0 3 3l1-2 3 1v3c-6 1-10-3-9-9z" fill="#fff"/></svg>+1 234 567 890</div>
  <div class="contact" style="top:210px"><svg width="12" height="12" viewBox="0 0 12 12"><circle cx="6" cy="6" r="5" fill="none" stroke="#fff" stroke-width="1.2"/><path d="M1 6h10M6 1c-3 3-3 7 0 10M6 1c3 3 3 7 0 10" fill="none" stroke="#fff" stroke-width=".9"/></svg>www.yourwebsite.com</div>
  <div class="contact" style="top:232px"><svg width="12" height="12" viewBox="0 0 12 12"><rect x="1" y="2.5" width="10" height="7" fill="#fff"/><path d="M1 3l5 4 5-4" fill="none" stroke="#0f6a78" stroke-width="1"/></svg>addyouremail@here.com</div>
  <div class="contact" style="top:254px"><svg width="12" height="12" viewBox="0 0 12 12"><path d="M6 11S2 7 2 4.5a4 4 0 0 1 8 0C10 7 6 11 6 11z" fill="#fff"/><circle cx="6" cy="4.5" r="1.5" fill="#0f6a78"/></svg>Add your location here</div>
</section>

</main>
</body>
</html>
```